Bold, Modern, Clean "Quarvenstretch.com" website

Why we stand out?
We are a male and female mobile massage team. Our names are Todd and Lise. 
Quarven Tide is a Seattle based mobile massage service. Our massage is offered to the community with a goal of facilitating balance within each individual. We specialize in integrated Pain management, and sports/medical massage therapy. Every client's first assessment is attended by our male and female massage therapist team. Depending on the goals identified for an individual determines which therapist will be assigned to provide treatment, if not both.

Our passion...
Here at Quarven Tide, we have a great passion for Postural Resoration and how it is integrated into an individual's Massage treatment. We pride ourselves in being natural facilitators of healing, which takes the ego of the therapist out of the client's healing process. We strive to deliver the best massage possible by including modalities such as Neuromuscular, Myofascial release, spontaneous muscle release, postural restoration, orthopedic, and medical massage.

Our education...

We are both Graduates of Halvenor, school of massage therapy. We have continuing education in medical massage, myofacial release, trigger point therapy, postural restoration, anatomy, and spontaneous muscle release. Lise is also a Certified Yoga Instructor, which amplifies her experience with flexibility and strength as it pertains to each individual. Todd's passion is Massage, stretching, and strength training to encourage postural restoration and realignment.

Our rates-

Our rates are $75/ 60 minutes, $95/ 90 minutes, and $120/ 120 minutes.

Education-
Both Lise and I worked as behavioral health professionals that specialized in life skills mentoring for youth who had experienced different types of trauma. This led us both to want to help others in a different environment, where individuals can be empowered to take responsibility over their own healing. To us, massage is a type of manipulation physical therapy, that encourages healing on many levels.

Advice to any massage client-
The most important thing to 'us', as Licenced providers is to get you on to our table to show you our skills. But a good therapist never forgets that it's not about what we do for you, but what we can facilitate for you. Your health and healing has nothing to do with us. It is yours, not ours. Identify what your goals are with any Therapist, and know what the end looks like. Progress should be tangible, such as range of motion, and decreased pain.

5/5 stars Massage Therapy
Verified Review

Lise and Todd at Quarven Tide are awesome! I recently had open heart surgery, and Lise worked on me to increase my range of motion while helping with the pinched nerve from my arm being in the same position for so long during my surgery. My wife drives a lot for work, and Todd has helped decrease her neck and lower back pain immensely. They are seriously the best therapists I have ever worked with. I would recommend them to anyone who needs anything from stress relief to a medical massage treatment. They are professional, up beat, easy going, and always on time. And, I love that they meet us where ever we like! We did a staycation recently, where they came to our hotel to give us relaxation massages. Although usually they come to our home, where we focus on pain related issues. We will continue to work with them for a long, long time.

Bressa K. on December 17, 2015

Target Market(s)

Mobile massage therapy clients

Industry/Entity Type

Massage Therapy

Font styles to use
Serif
Sans Serif

Requirements
Must have
• Please add or remove any information that would help the presentation of our website. Our logo is posted below, please include into the website.
• Please include a contact field that includes, quarvenstretch@mailbrook.net,
• (206) 555-0194
• We have also included our own stock photos, as well as a photo of Todd and Lise. Please include a cropped photo of both massage therapists.

```html
<!DOCTYPE html>
<html lang="en">
<head>
<meta charset="utf-8">
<title>Quarven Tide Mobile Massage</title>
<link rel="stylesheet" href="https://fonts.googleapis.com/css2?family=Open+Sans:wght@400;600;700&family=Raleway:wght@400;500;700&family=Pinyon+Script&display=swap">
<style>
  :root {
    --ink: #111111;
    --header-bg: #1b1b1b;
    --accent: #1a97c9;
    --accent-soft: #2fb0d8;
    --light-bg: #f0f0f0;
    --news-bg: #ebebeb;
    --white: #ffffff;
    --body-text: #444444;
    --muted: #8a8a8a;
    --footer-bg: #050505;
  }
  * { box-sizing: border-box; margin: 0; padding: 0; }
  html, body { width: 667px; height: 1200px; overflow: hidden; }
  body { position: relative; background: var(--white); font-family: "Open Sans", Arial, sans-serif; color: var(--ink); }
  section, header, footer { position: absolute; left: 0; width: 667px; }

  /* Header */
  .site-header { top: 0; height: 52px; background: var(--header-bg); }
  .brand { position: absolute; left: 24px; top: 8px; display: flex; align-items: center; gap: 6px; }
  .brand-dot { width: 34px; height: 34px; border-radius: 50%; background: var(--accent); }
  .brand-name { font-family: "Open Sans", Arial, sans-serif; font-weight: 700; font-size: 10px; color: var(--white); width: 48px; line-height: 1.15; }
  .main-nav { position: absolute; left: 116px; top: 22px; display: flex; gap: 0; }
  .main-nav a { font-family: "Open Sans", Arial, sans-serif; font-size: 6.4px; font-weight: 600; color: var(--white); text-decoration: none; margin-right: 21px; white-space: nowrap; }
  .main-nav a.active { color: var(--accent); position: relative; }
  .main-nav a.active::after { content: ""; position: absolute; left: -2px; right: -2px; top: 12px; height: 1px; background: var(--accent); }

  /* Hero */
  .hero { top: 52px; height: 337px; }
  .hero-photo { position: absolute; inset: 0; background: radial-gradient(ellipse at 70% 30%, #b99476 0%, #6e4e38 40%, #2e221b 80%); }
  .hero-shade { position: absolute; inset: 0; background: rgba(0,0,0,0.25); }
  .hero-title { position: absolute; left: 0; width: 100%; top: 120px; text-align: center; font-family: "Pinyon Script", cursive; font-size: 42px; color: var(--white); }
  .hero-title .amp { color: var(--accent); }
  .hero-text { position: absolute; left: 126px; width: 415px; top: 186px; text-align: center; font-size: 8.4px; line-height: 11.5px; color: var(--white); }
  .btn-solid { position: absolute; background: var(--accent); color: var(--white); font-size: 8px; font-weight: 600; display: flex; align-items: center; justify-content: center; text-decoration: none; }
  .hero .btn-solid { left: 287px; top: 232px; width: 77px; height: 24px; }
  .slider-dots { position: absolute; left: 29px; top: 318px; display: flex; gap: 7px; }
  .slider-dots span { width: 9px; height: 9px; border-radius: 50%; background: var(--white); }
  .slider-dots span.current { background: transparent; border: 1.5px solid var(--accent); }

  /* Welcome */
  .welcome { top: 389px; height: 172px; background: var(--light-bg); text-align: center; }
  .section-title { font-family: "Raleway", Arial, sans-serif; font-weight: 400; color: var(--ink); }
  .section-title em { font-style: normal; color: var(--accent); }
  .welcome .section-title { position: absolute; top: 27px; width: 100%; font-size: 20px; }
  .welcome-text { position: absolute; left: 56px; width: 555px; top: 62px; font-size: 6.4px; line-height: 13px; color: var(--body-text); }
  .btn-outline { position: absolute; left: 304px; top: 122px; width: 65px; height: 26px; border: 1px solid var(--accent); color: var(--accent); font-size: 6.4px; display: flex; align-items: center; justify-content: center; text-decoration: none; }

  /* Specialties */
  .specialties { top: 561px; height: 219px; }
  .specialties .section-title { position: absolute; top: 37px; width: 100%; text-align: center; font-size: 19px; }
  .spec-card { position: absolute; top: 80px; width: 306px; height: 132px; overflow: hidden; }
  .spec-card.pain { left: 27px; background: linear-gradient(135deg, #9a948c, #6f6a63 60%, #5c5a55); }
  .spec-card.sports { left: 335px; background: linear-gradient(135deg, #3fb4dc, #22a1d0 60%, #1a8fbe); }
  .spec-frame { position: absolute; inset: 5px; border: 1px solid rgba(255,255,255,0.7); }
  .spec-name { position: absolute; left: 0; width: 100%; text-align: center; font-family: "Open Sans", Arial, sans-serif; font-weight: 600; font-size: 11.6px; color: var(--white); }
  .pain .spec-name { top: 56px; left: -16px; }
  .sports .spec-name { top: 52px; }
  .spec-icon { position: absolute; left: 143px; top: 25px; }
  .spec-text { position: absolute; left: 30px; width: 246px; top: 75px; text-align: center; font-size: 6.4px; line-height: 8px; color: var(--white); }
  .btn-small { position: absolute; left: 116px; top: 99px; width: 58px; height: 15px; background: var(--white); color: var(--accent); font-size: 6px; display: flex; align-items: center; justify-content: center; gap: 3px; text-decoration: none; }

  /* Video */
  .video { top: 780px; height: 182px; background: linear-gradient(90deg, #222 0%, #3b332e 55%, #5a4d44 100%); }
  .video-title { position: absolute; left: 119px; top: 52px; font-family: "Open Sans", Arial, sans-serif; font-weight: 700; font-size: 18px; color: var(--white); }
  .video-text { position: absolute; left: 119px; top: 82px; width: 250px; font-size: 9px; line-height: 13px; color: var(--white); }
  .video .btn-solid { left: 120px; top: 122px; width: 85px; height: 21px; }
  .play-icon { position: absolute; left: 434px; top: 293px; }

  /* Newsletter */
  .newsletter { top: 962px; height: 168px; background: var(--news-bg); }
  .newsletter .section-title { position: absolute; top: 22px; width: 100%; text-align: center; font-size: 26px; }
  .email-field { position: absolute; left: 153px; top: 66px; width: 251px; height: 40px; background: var(--white); border: 1px solid #dcdcdc; font-size: 8px; color: #555; padding-left: 15px; display: flex; align-items: center; }
  .subscribe-btn { position: absolute; left: 414px; top: 66px; width: 110px; height: 40px; background: #a9a9a9; color: var(--white); font-size: 13px; display: flex; align-items: center; justify-content: center; }
  .newsletter-text { position: absolute; left: 170px; width: 327px; top: 120px; text-align: center; font-size: 7.8px; line-height: 13px; color: var(--body-text); }

  /* Footer */
  .site-footer { top: 1130px; height: 70px; background: var(--footer-bg); }
  .footer-links { position: absolute; width: 100%; top: 24px; text-align: center; font-size: 6.2px; color: var(--muted); }
  .copyright { position: absolute; width: 100%; top: 38px; text-align: center; font-size: 5.2px; color: #555; }
  .social { position: absolute; left: 539px; top: 27px; display: flex; gap: 6px; }
  .social span { width: 15px; height: 15px; border: 1px solid var(--accent); }
  .social span.filled { background: var(--accent); }
</style>
</head>
<body>
  <header class="site-header">
    <div class="brand"><span class="brand-dot"></span><span class="brand-name">Quarven Tide</span></div>
    <nav class="main-nav">
      <a class="active" href="#">HOME</a>
      <a href="#">WHY WE STAND OUT?</a>
      <a href="#">OUR PASSION</a>
      <a href="#">EDUCATION</a>
      <a href="#">OUR RATES</a>
      <a href="#">5/5 STARS MASSAGE THERAPY</a>
      <a href="#">TESTIMONIALS</a>
      <a href="#">CONTACT</a>
    </nav>
  </header>

  <section class="hero">
    <div class="hero-photo" role="img" aria-label="Woman relaxing on a massage table receiving a head massage by candlelight"></div>
    <div class="hero-shade"></div>
    <h1 class="hero-title">Beauty <span class="amp">&amp;</span> Velaxation</h1>
    <p class="hero-text">Lorem ipsum dolor sit amet, consectetur adipiscing elit, sed do eiusmod tempor incididunt ut labore et dolore magna aliqua. Ut enim ad minim veniamexercitation enim ad minim veniamexercitation ullamco laboris nisi ut aliquip ex ea commodo consequat.</p>
    <a class="btn-solid" href="#">READ MORE</a>
    <div class="slider-dots"><span></span><span></span><span></span><span class="current"></span><span></span></div>
  </section>

  <section class="welcome">
    <h2 class="section-title">Welcome to <em>Quarven Tide Mobile Massage</em></h2>
    <p class="welcome-text">Lorem ipsum dolor sit amet, consectetur adipiscing elit, sed do eiusmod tempor incididunt ut labore et dolore magna aliqua. Ut enim ad minim veniam, quis nostrud exercitation ullamco laboris nisi ut aliquip ex ea commodo consequat. Duis aute irure dolor in reprehenderit in voluptate velit esse cillum dolore eu fugiat nulla pariatur. Excepteur sint occaecat cupidatat non proident, sunt in culpa qui officia deserunt mollit anim id est laborum.</p>
    <a class="btn-outline" href="#">READ MORE</a>
  </section>

  <section class="specialties">
    <h2 class="section-title">We are <em>Specialize in</em></h2>
    <div class="spec-card pain" role="img" aria-label="Woman stretching her neck and shoulders in a treatment room">
      <div class="spec-frame"></div>
      <h3 class="spec-name">INTEGRATED PAIN MANAGEMENT</h3>
    </div>
    <div class="spec-card sports">
      <div class="spec-frame"></div>
      <svg class="spec-icon" width="20" height="20" viewBox="0 0 20 20" aria-hidden="true">
        <path d="M3 17 L11 9" stroke="#fff" stroke-width="3" stroke-linecap="round"/>
        <circle cx="13.5" cy="6.5" r="4.5" fill="#fff"/>
        <circle cx="15" cy="5" r="2" fill="#22a1d0"/>
      </svg>
      <h3 class="spec-name">SPORTS/MEDICAL MASSAGE THERAPY</h3>
      <p class="spec-text">Lorem ipsum dolor sit amet, consectetur adipiscing elit, sed do eiusmod tempor incididunt ut labore et dolore magna aliqua. Ut enim ad minim veniam,</p>
      <a class="btn-small" href="#">READ MORE <svg width="4" height="5" viewBox="0 0 4 5" aria-hidden="true"><path d="M0 0 L4 2.5 L0 5Z" fill="#1a97c9"/></svg></a>
    </div>
  </section>

  <section class="video" role="img" aria-label="Therapist's hands massaging a client's back in dim light">
    <h2 class="video-title">LATEST MASSAGE VIDEO</h2>
    <p class="video-text">Lorem ipsum dolor sit amet, consectetur adipiscing elit, sed do eiusmod tempor</p>
    <a class="btn-solid" href="#">LEARN MORE</a>
  </section>
  <svg class="play-icon" width="50" height="50" viewBox="0 0 50 50" aria-label="Play video">
    <circle cx="25" cy="25" r="22" fill="none" stroke="#8a8a8a" stroke-width="3"/>
    <path d="M19 14 L36 25 L19 36Z" fill="#8a8a8a"/>
  </svg>

  <section class="newsletter">
    <h2 class="section-title">Subscribe to our Newsletter</h2>
    <div class="email-field">Email Address</div>
    <div class="subscribe-btn">Subscibe</div>
    <p class="newsletter-text">Lorem ipsum dolor sit amet, consectetur adipiscing elit, sed do eiusmod tempor incididunt labore et dolore magna aliqua.</p>
  </section>

  <footer class="site-footer">
    <p class="footer-links">Home &nbsp;/&nbsp; About Us &nbsp;/&nbsp; Our Services &nbsp;/&nbsp; Testimonials &nbsp;/&nbsp; Gallery &nbsp;/&nbsp; Contact</p>
    <p class="copyright">Copyright @ Norvel Studio - 2015</p>
    <div class="social"><span></span><span></span><span></span><span class="filled"></span><span></span></div>
  </footer>
</body>
</html>
```